Enlargement project

We would like to create an enlargement of the attached business card design, so that we are able to print hi-res business cards from it,

The end result we are after is an illustrator template that contains hi-res graphics and text that we can edit to insert people's names, job titles, phone and email details

The two colours used within the design are:

Pantone 350 (green)
Panton 484 (red)

The fonts used are;

Futura Medium
Futura Bk BT Italic

Industry/Entity Type

Business

```html
<!DOCTYPE html>
<html lang="en">
<head>
<meta charset="utf-8">
<title>Wardline business card – front and back</title>
<link href="https://fonts.googleapis.com/css2?family=Jost:ital,wght@0,400;0,500;0,600;1,400&display=swap" rel="stylesheet">
<style>
  :root {
    --brand-red: #b5161b;
    --card-dark: #141414;
    --card-mid: #4a4a4a;
    --soft-grey: #9a9a9a;
    --light-grey: #c9c9c9;
    --white: #ffffff;
    --page: #ffffff;
  }
  * { box-sizing: border-box; margin: 0; padding: 0; }
  html, body {
    width: 1200px; height: 337px; overflow: hidden;
    background: var(--page);
    font-family: "Jost", "Futura", sans-serif;
  }
  .sheet { position: relative; width: 1200px; height: 337px; }
  .card {
    position: absolute; top: 7px; height: 322px; overflow: hidden;
    background: radial-gradient(ellipse at 38% 22%, var(--card-mid) 0%, #2b2b2b 45%, var(--card-dark) 100%);
  }
  .card--front { left: 7px; width: 532px; }
  .card--back { left: 663px; width: 528px; }

  /* front */
  .front-band {
    position: absolute; left: 0; bottom: 0; width: 500px; height: 10px;
    background: var(--brand-red);
  }
  .front-band-end {
    position: absolute; right: 0; bottom: 0; width: 32px; height: 10px;
    background: var(--soft-grey);
  }
  .front-mark {
    position: absolute; left: 289px; top: 106px; width: 136px; height: 134px;
    background: var(--brand-red);
  }
  .front-name {
    position: absolute; left: 100px; top: 138px;
    font-size: 56px; font-weight: 600; line-height: 1;
    color: var(--soft-grey); letter-spacing: 0.5px;
  }

  /* back */
  .back-logo {
    position: absolute; left: 0; right: 0; top: 46px;
    display: flex; justify-content: center; align-items: center; gap: 12px;
  }
  .back-name {
    font-size: 36px; font-weight: 600; color: var(--white); line-height: 1;
  }
  .back-mark { width: 46px; height: 46px; background: var(--brand-red); }
  .person {
    position: absolute; left: 0; right: 0; top: 140px; text-align: center;
  }
  .person-name {
    font-size: 22px; font-weight: 600; color: var(--white); line-height: 1.2;
  }
  .person-role {
    font-size: 22px; font-weight: 400; color: var(--brand-red); line-height: 1.2;
  }
  .divider {
    position: absolute; left: 0; right: 0; top: 217px; height: 9px;
    background: var(--light-grey);
  }
  .contact-band {
    position: absolute; left: 0; right: 0; top: 226px; bottom: 0;
    background: var(--brand-red);
  }
  .web {
    position: absolute; left: 40px; top: 40px;
    font-size: 22px; font-weight: 600; color: var(--white);
  }
  .phones {
    position: absolute; left: 340px; top: 16px; list-style: none;
    font-size: 18px; color: var(--white); line-height: 27px;
  }
</style>
</head>
<body>
<main class="sheet">
  <section class="card card--front" aria-label="Card front">
    <div class="front-mark"></div>
    <p class="front-name">Wardline</p>
    <div class="front-band"></div>
    <div class="front-band-end"></div>
  </section>

  <section class="card card--back" aria-label="Card back">
    <div class="back-logo">
      <span class="back-name">Wardline</span>
      <span class="back-mark"></span>
    </div>
    <div class="person">
      <p class="person-name">Daniel</p>
      <p class="person-role">Technical Operations</p>
    </div>
    <div class="divider"></div>
    <div class="contact-band">
      <p class="web">www.wardline.net</p>
      <ul class="phones">
        <li>T 03 5550</li>
        <li>F 03 5550</li>
        <li>D 03 55 50</li>
      </ul>
    </div>
  </section>
</main>
</body>
</html>
```